New Church Home Page and Content Page Design

Our church, Cedar Hollow Baptist Church www.chbcfenway.example, needs an update for our online presence. The homepage design should provide the following 4 pieces of information above the fold:
1. Church location - 47 Linden Brook Lane in Chappaqua, NY, USA.
2. Service times and types Sunday school, children's church, etc..
3. A space for some text describing us and our beliefs - a Bible believing independent Baptist church.
4. photos of our members to give visitors an impression of what kind of people attend our church - a friendly group of culturally diverse people who love Jesus.

In addition to the homepage we need a design for internal pages of general content. The content page design should provide a lot of room for content and prominent navigation area. We will use this design to host pages with content such as:
A full description of our beliefs
A photo gallery
An event calendar
Embedded audio and video of past sermons
A member directory
etc.
Updates

Thanks everyone for your submissions. I'll be meeting with our Pastor tomorrow. I am working as fast as I can to review all the designs and come up with a short list for him. A decision should be close behind.

Target Market(s)

Local people looking for a church.

Industry/Entity Type

Church

Requirements
Must have
• 1. Place to show church location - Westchester county, New York State, USA.
2. Place to list service times and types.
3. A space for some text describing us and our beliefs.
4. A place to display photos of our members (see also the nice to have section)
Nice to have
• Would be great if the member photos (#4 in must have section) displayed the images in some innovative way. I rather not have an ordinary carousel of images.

```html
<!DOCTYPE html>
<html lang="en">
<head>
<meta charset="utf-8">
<title>Cedar Hollow Baptist Church</title>
<link rel="stylesheet" href="https://fonts.googleapis.com/css2?family=Open+Sans:wght@400;600&display=swap">
<style>
:root{
  --navy:#173d65;
  --link:#2d6497;
  --nav-top:#2f6fa6;
  --nav-bottom:#123f6c;
  --nav-active:#4c86b8;
  --nav-divider:#0c2d4f;
  --text:#6a6a6a;
  --text-dark:#555;
  --rule:#dcdcdc;
  --panel:#f2f2f2;
  --footer:#383838;
  --footer-text:#b9b9b9;
  --social:#6c6c6c;
}
*{box-sizing:border-box;margin:0;padding:0}
html,body{width:1078px;height:1200px;overflow:hidden;background:#fff}
body{position:relative;font-family:"Open Sans",Arial,sans-serif;color:var(--text)}
.abs{position:absolute}

/* header */
.brand{left:92px;top:18px;width:200px;font-weight:600;font-size:19px;line-height:21px;color:var(--navy)}
.contact-block{right:122px;top:27px;text-align:right}
.contact-block .location{font-size:13px;color:var(--text-dark)}
.contact-block .phone{font-size:18px;font-weight:600;color:var(--navy);margin-top:2px}
.mail-icon{left:966px;top:34px;width:23px;height:25px}

/* nav */
.main-nav{left:0;top:104px;width:1078px;height:43px;background:linear-gradient(var(--nav-top),var(--nav-bottom))}
.main-nav ul{list-style:none;position:absolute;left:92px;top:0;height:43px;display:flex;border-right:1px solid var(--nav-divider)}
.main-nav li{height:43px;line-height:43px;color:#e7eef6;font-size:13px;text-align:center;border-left:1px solid var(--nav-divider)}
.main-nav li.active{background:linear-gradient(#5b93c2,#3a72a4);color:#fff;border-left:none}

/* hero */
.hero{left:89px;top:158px;width:901px;height:349px;background:linear-gradient(180deg,#9cc07e 0%,#7b6a55 40%,#6d6050 60%,#4f7a3a 100%)}
.hero-caption{left:99px;top:317px;height:31px;padding:0 10px;background:rgba(0,0,0,.7);color:#fff;font-size:21px;line-height:31px}
.hero-dots{left:503px;top:475px;width:70px;height:14px;background:rgba(0,0,0,.55);border-radius:7px;display:flex;gap:9px;justify-content:center;align-items:center}
.hero-dots span{width:8px;height:8px;border-radius:50%;background:#fff}
.hero-dots span.current{background:transparent;border:1.5px solid #fff}

/* services */
.service{width:206px;text-align:center}
.service .photo{width:206px;height:124px}
.service h3{margin-top:8px;font-size:13px;font-weight:400;color:var(--link);line-height:20px}
.service p{font-size:13px;color:var(--text-dark);line-height:20px;margin-top:1px}
.divider{left:89px;top:741px;width:901px;height:1px;background:var(--rule)}

/* welcome */
.welcome{left:94px;top:772px;width:620px}
.welcome h1{font-size:21px;font-weight:600;color:var(--navy);line-height:26px;margin-bottom:14px}
.welcome p{font-size:12px;line-height:18.6px;margin-bottom:8px}

.newsletter{left:93px;top:973px;width:611px;height:97px;background:#f4f4f4;border:1px solid #dedede;border-radius:3px;overflow:hidden}
.newsletter h2{position:absolute;left:22px;top:17px;font-size:17px;font-weight:400;color:var(--link)}
.field{position:absolute;top:45px;width:196px;height:31px;background:#fff;border:1px solid #d6d6d6;border-radius:3px;font-size:12px;color:#a2a2a2;line-height:29px;padding-left:14px}
.subscribe{position:absolute;left:434px;top:45px;width:85px;height:32px;background:linear-gradient(#555,#333);border-radius:3px;color:#fff;font-size:13px;text-align:center;line-height:32px}
.newsletter .photo{position:absolute;right:0;top:0;width:68px;height:97px;background:linear-gradient(90deg,#eee,#5a5a5a)}

/* members */
.members-title{left:742px;top:776px;font-size:13px;font-weight:600;color:var(--link)}
.members{left:744px;top:800px;width:243px;height:272px;background:var(--panel)}
.member{position:absolute;left:14px;width:225px}
.member .photo{width:70px;height:70px;border:3px solid #fff;box-shadow:0 1px 3px rgba(0,0,0,.3)}
.member h4{position:absolute;left:85px;top:0;font-size:12px;font-weight:400;color:var(--navy)}
.member p{position:absolute;left:85px;top:19px;font-size:11px;line-height:15.5px;color:var(--text-dark);width:140px}

/* footer */
.site-footer{left:0;top:1108px;width:1078px;height:92px;background:var(--footer)}
.footer-links{position:absolute;left:91px;top:21px;font-size:11.5px;color:var(--footer-text);letter-spacing:.2px}
.footer-links span.sep{color:#777;margin:0 7px}
.copyright{position:absolute;left:91px;top:53px;font-size:11.5px;color:var(--footer-text)}
.social{position:absolute;left:871px;top:33px;display:flex;gap:7px}
.social span{width:24px;height:24px;border-radius:50%;background:var(--social)}
</style>
</head>
<body>

<header>
  <div class="abs brand">Cedar Hollow<br>Baptist Church</div>
  <div class="abs contact-block">
    <div class="location">Westchester county, New York State, USA.</div>
    <div class="phone">Call us : 914.555.0147</div>
  </div>
  <svg class="abs mail-icon" viewBox="0 0 23 25" aria-label="Email">
    <rect x="1" y="1" width="21" height="23" fill="#8a8a8a" stroke="#cfcfcf"/>
    <circle cx="11.5" cy="11" r="5" fill="none" stroke="#fff" stroke-width="1.6"/>
    <circle cx="11.5" cy="11" r="1.8" fill="none" stroke="#fff" stroke-width="1.3"/>
  </svg>
</header>

<nav class="abs main-nav">
  <ul>
    <li class="active" style="width:84px">HOME</li>
    <li style="width:117px">ABOUT US</li>
    <li style="width:116px">CALENDAR</li>
    <li style="width:119px">MINISTRIES</li>
    <li style="width:140px">SERVICE TIMES</li>
    <li style="width:189px">SERMONS AND MEDIA</li>
    <li style="width:129px">CONTACT US</li>
  </ul>
</nav>

<section>
  <div class="abs hero" role="img" aria-label="Photo of the stone church building among green trees"></div>
  <div class="abs hero-caption">Suspendisse luctus lobortis nunc porttitor</div>
  <div class="abs hero-dots"><span class="current"></span><span></span><span></span><span></span></div>
</section>

<section>
  <div class="abs service" style="left:91px;top:525px">
    <div class="photo" role="img" aria-label="Photo of members holding candles" style="background:linear-gradient(135deg,#4a3a2a,#9a7a55,#3a2a1c)"></div>
    <h3>COFFEE AND FELLOWSHIP</h3><p>TIME - 9:45 AM</p>
  </div>
  <div class="abs service" style="left:321px;top:525px">
    <div class="photo" role="img" aria-label="Photo of a bright hall with seated congregation" style="background:linear-gradient(180deg,#8a6a4a,#e8e4dc 45%,#6a5a4e)"></div>
    <h3>SUNDAY SCHOOL</h3><p>TIME - 10:00 AM</p>
  </div>
  <div class="abs service" style="left:551px;top:525px">
    <div class="photo" role="img" aria-label="Photo of a lit candle at morning worship" style="background:linear-gradient(135deg,#c8a878,#e8dccb 50%,#6a4a2a)"></div>
    <h3>SUNDAY MORNING WORSHIP</h3><p>TIME - 11:00 AM</p>
  </div>
  <div class="abs service" style="left:782px;top:525px">
    <div class="photo" role="img" aria-label="Photo of praying hands over an open Bible" style="background:linear-gradient(180deg,#c23a3a,#d8d2cc 55%,#eeeae4)"></div>
    <h3>WEDNESDAY BIBLE STUDY &amp;<br>PRAYER TIME</h3><p>TIME - 7:00 PM</p>
  </div>
  <div class="abs divider"></div>
</section>

<main class="abs welcome">
  <h1>WELCOME TO CEDAR HOLLOW BAPTIST CHURCH</h1>
  <p>Quisque aliquam arcu lectus, nec bibendum turpis dapibus pellentesque. Pellentesque vitae tincidunt quam, et elementum nunc. Quisque risus ligula, vestibulum at suscipit eu, bibendum vitae neque. Fusce erat libero, sollicitudin rutrum mi elementum, vehicula auctor mi.</p>
  <p>Proin sapien purus, varius ultricies felis posuere, lacinia ultrices magna. Mauris pharetra dapibus leo at laoreet. Quisque sit amet mauris id velit feugiat imperdiet quis at eros. Mauris vestibulum dapibus massa, ut consequat ipsum ullamcorper ut. Mauris pulvinar a leo et ultricies. Etiam sollicitudin condimentum mauris id tempus. Donec rutrum turpis erat, eu semper leo ultricies nec.</p>
</main>

<section class="abs newsletter">
  <h2>NEWSLETTER SUBSCRIBE</h2>
  <div class="field" style="left:27px">Name</div>
  <div class="field" style="left:233px">E-mail</div>
  <div class="subscribe">Subscribe</div>
  <div class="photo" role="img" aria-label="Photo of a man in prayer"></div>
</section>

<aside>
  <div class="abs members-title">OUR MEMBERS</div>
  <div class="abs members">
    <div class="member" style="top:16px">
      <div class="photo" role="img" aria-label="Member photo" style="background:linear-gradient(135deg,#8a5a3a,#d8cfc4)"></div>
      <h4>Vivamus porttitor</h4><p>Sem ac varius rhoncus tellus urna dictum augue</p>
    </div>
    <div class="member" style="top:101px">
      <div class="photo" role="img" aria-label="Member photo" style="background:linear-gradient(135deg,#b86a4a,#e8d8c8 50%,#6a3a7a)"></div>
      <h4>Vivamus porttitor</h4><p>Sem ac varius rhoncus tellus urna dictum augue</p>
    </div>
    <div class="member" style="top:185px">
      <div class="photo" role="img" aria-label="Member photo" style="background:linear-gradient(135deg,#2a2a2a,#7a5a44,#1e1e1e)"></div>
      <h4>Vivamus porttitor</h4><p>Sem ac varius rhoncus tellus urna dictum augue</p>
    </div>
  </div>
</aside>

<footer class="abs site-footer">
  <div class="footer-links">Home<span class="sep">|</span>About us<span class="sep">|</span>Calendar<span class="sep">|</span>Ministries<span class="sep">|</span>Service Times<span class="sep">|</span>Sermons and Media<span class="sep">|</span>Contact Us</div>
  <div class="copyright">Copyright &copy; 2014 &nbsp;Cedar Hollow Baptist Church. &nbsp;All rights reserved.</div>
  <div class="social">
    <span aria-label="Social link"></span><span aria-label="Social link"></span><span aria-label="Social link"></span><span aria-label="Social link"></span>
  </div>
</footer>

</body>
</html>
```